Velvor IT Services Business Card

Velvor IT Services are a Perth based IT Services company. We would like to incorporate our company logo (attached) and stick with the blue that is in that design. I would like a clean look design that isn't too busy, yet creates a lasting image that is instantly recognisable in the recipients mind.

Target Market(s)

The target audience is small/medium business owners.

Industry/Entity Type

Business

Font styles to use
Serif
Sans Serif

Colors

Designer to choose colors to be used in the design.

Requirements
Must have
• The design should include:
Business name: Velvor IT Services
Directors Name: Marcus Dredge
Phone Number: 0483 906 452
Email: support@velvorit.com.au
Website: www.velvorit.com.au

```html
<!DOCTYPE html>
<html lang="en">
<head>
<meta charset="utf-8">
<title>Velvor IT Services Business Card</title>
<link rel="stylesheet" href="https://fonts.googleapis.com/css2?family=Open+Sans:wght@400;600;700&display=swap">
<style>
  :root {
    --bg: #e4e4e4;
    --brand-blue: #1f45b0;
    --brand-blue-dark: #16308a;
    --sky-deep: #1b9be3;
    --sky-light: #c9ecfb;
    --card-white: #ffffff;
    --text-grey: #555a60;
    --pattern-grey: #c4c6c9;
  }
  html, body {
    margin: 0;
    width: 1200px;
    height: 1200px;
    overflow: hidden;
    background: var(--bg);
    font-family: "Open Sans", Arial, sans-serif;
  }
  .canvas {
    position: relative;
    width: 1200px;
    height: 1200px;
  }
  .card {
    position: absolute;
    left: 180px;
    width: 840px;
    height: 480px;
    border-radius: 6px;
    overflow: hidden;
    box-shadow: 0 6px 24px rgba(0,0,0,0.12);
  }
  /* Front */
  .card-front {
    top: 90px;
    background: radial-gradient(ellipse at 55% 55%, var(--sky-light) 0%, #7fcdf3 45%, var(--sky-deep) 100%);
  }
  .front-brand {
    position: absolute;
    left: 0; right: 0;
    top: 210px;
    display: flex;
    justify-content: center;
    align-items: center;
    gap: 18px;
  }
  .brand-mark {
    width: 26px;
    height: 26px;
    background: var(--brand-blue);
  }
  .brand-name {
    font-weight: 700;
    color: var(--brand-blue);
    white-space: nowrap;
  }
  .front-brand .brand-name { font-size: 52px; }

  /* Back */
  .card-back {
    top: 630px;
    background: var(--card-white);
  }
  .name-bar {
    position: absolute;
    left: 110px;
    top: 100px;
    width: 400px;
    height: 78px;
    border-radius: 12px;
    background: linear-gradient(90deg, var(--brand-blue-dark), #2f63d6);
    display: flex;
    align-items: center;
    padding-left: 30px;
    box-sizing: border-box;
  }
  .director-name {
    color: #fff;
    font-size: 28px;
    font-weight: 400;
  }
  .back-brand {
    position: absolute;
    right: 60px;
    top: 120px;
    display: flex;
    align-items: center;
    gap: 12px;
  }
  .back-brand .brand-name { font-size: 28px; }
  .back-brand .brand-mark { width: 18px; height: 18px; }
  .contact-list {
    position: absolute;
    left: 110px;
    top: 205px;
    margin: 0;
    padding: 0;
    list-style: none;
  }
  .contact-item {
    display: flex;
    align-items: center;
    gap: 14px;
    height: 36px;
    font-size: 24px;
    color: var(--text-grey);
  }
  .contact-icon {
    width: 22px;
    height: 22px;
    flex: none;
  }
  .corner-pattern {
    position: absolute;
    right: 0;
    bottom: 0;
    width: 520px;
    height: 110px;
    background: linear-gradient(90deg, rgba(196,198,201,0) 0%, var(--pattern-grey) 60%, #b3b5b8 100%);
  }
</style>
</head>
<body>
<main class="canvas">

  <section class="card card-front" aria-label="Card front">
    <div class="front-brand">
      <span class="brand-mark"></span>
      <span class="brand-name">Velvor IT Services</span>
    </div>
  </section>

  <section class="card card-back" aria-label="Card back">
    <div class="name-bar">
      <span class="director-name">Marcus Dredge</span>
    </div>

    <div class="back-brand">
      <span class="brand-mark"></span>
      <span class="brand-name">Velvor IT Services</span>
    </div>

    <ul class="contact-list">
      <li class="contact-item">
        <svg class="contact-icon" viewBox="0 0 22 22" aria-hidden="true">
          <rect width="22" height="22" rx="4" fill="#1f45b0"/>
          <path d="M7 5 L9.5 5 L10.5 8 L9 9.2 Q10.5 12 12.8 13 L14 11.5 L17 12.5 L17 15 Q16 16.5 14 16 Q8 14 6 8 Q5.6 6 7 5 Z" fill="#fff"/>
        </svg>
        <span>0483 906 452</span>
      </li>
      <li class="contact-item">
        <svg class="contact-icon" viewBox="0 0 22 22" aria-hidden="true">
          <rect width="22" height="22" rx="4" fill="#1f45b0"/>
          <rect x="5" y="7" width="12" height="8.5" fill="none" stroke="#fff" stroke-width="1.5"/>
          <path d="M5 7 L11 12 L17 7" fill="none" stroke="#fff" stroke-width="1.5"/>
        </svg>
        <span>support@velvorit.com.au</span>
      </li>
      <li class="contact-item">
        <svg class="contact-icon" viewBox="0 0 22 22" aria-hidden="true">
          <rect width="22" height="22" rx="4" fill="#1f45b0"/>
          <circle cx="11" cy="11" r="6" fill="none" stroke="#fff" stroke-width="1.4"/>
          <ellipse cx="11" cy="11" rx="2.6" ry="6" fill="none" stroke="#fff" stroke-width="1.2"/>
          <line x1="5" y1="11" x2="17" y2="11" stroke="#fff" stroke-width="1.2"/>
        </svg>
        <span>www.velvorit.com.au</span>
      </li>
    </ul>

    <div class="corner-pattern" role="img" aria-label="Grey decorative pixel-square pattern along the bottom edge"></div>
  </section>

</main>
</body>
</html>
```